Need design for an App.

The app in question is related to security and crime events with real time feed, engagement with friends and posting pictures, we want a sleak, minimal style. There are 11 or 12 screens to be made. We are adding video file as suggestion. We are not sure about colors so we accept suggestions. We are also adding the logo.

Reason: Just giving more time to designers. Thanks.

Industry/Entity Type

Security

Font styles to use
Sans Serif

Requirements
Must have
• The app must have a Login view; a new user view (with nickname, email and pass); a retrieve pass view; a menu view with options for alert configuration, send emergency alert and send report, a feed view with the most popular reports (3 worldwide at the top and near reports after), a profile view with avatar and personal reports, a send emergency alert view with a camera view; a configuration view when the user can put up to 5 contacts to send the alert to them;a send report view with camera and options to configure the camera; a edit report view where the user can see the 3 photos he will update and add a comment of those photos.
Nice to have
• Check the files we are open minds
Should not have
• old design

```html
<!DOCTYPE html>
<html lang="en">
<head>
<meta charset="utf-8">
<title>Vigilo – Sign Up Screen</title>
<link rel="stylesheet" href="https://fonts.googleapis.com/css2?family=Inter:wght@300;400;700&display=swap">
<style>
  :root {
    --canvas-bg: #ece6f8;
    --brand-red: #c41f3c;
    --brand-red-dark: #9d1830;
    --title-red: #c4203f;
    --ink: #0d0d0d;
    --muted: #5c6179;
    --white: #ffffff;
    --field-line: rgba(255, 255, 255, 0.45);
    --label-border: #43475c;
  }
  * { box-sizing: border-box; margin: 0; padding: 0; }
  html, body {
    width: 1200px; height: 1000px; overflow: hidden;
    background: var(--canvas-bg);
    font-family: "Inter", "Helvetica Neue", Arial, sans-serif;
  }
  .board { position: relative; width: 1200px; height: 1000px; }

  .board-heading { position: absolute; left: 68px; top: 66px; }
  .board-heading__name { font-size: 42px; font-weight: 700; color: var(--ink); letter-spacing: -0.5px; line-height: 1.1; }
  .board-heading__subtitle { font-size: 34px; font-weight: 400; color: var(--title-red); line-height: 1.2; }
  .board-heading__tagline { font-size: 22px; font-weight: 400; color: var(--muted); margin-top: 4px; }

  .screen-label {
    position: absolute; left: 770px; top: 842px; width: 364px; height: 78px;
    border: 1.5px solid var(--label-border); border-radius: 6px;
    display: flex; align-items: center; justify-content: center;
    font-size: 38px; font-weight: 300; color: var(--label-border);
  }

  .signup-screen {
    position: absolute; left: 420px; top: 90px; width: 360px; height: 720px;
    background: var(--brand-red); color: var(--white); overflow: hidden;
    box-shadow: 0 20px 40px rgba(60, 40, 90, 0.18);
  }

  .status-bar {
    height: 28px; padding: 0 10px; display: flex; align-items: center;
    justify-content: space-between; font-size: 12px; font-weight: 400;
  }
  .status-bar__carrier, .status-bar__battery { display: flex; align-items: center; gap: 5px; }

  .avatar { display: block; margin: 50px auto 0; width: 116px; height: 116px; }

  .signup-form { margin: 36px auto 0; width: 280px; }
  .signup-form__field {
    height: 56px; border-top: 1px solid var(--field-line);
    display: flex; align-items: center; justify-content: center;
    font-size: 19px; font-weight: 300;
  }
  .signup-form__field--password { letter-spacing: 3px; font-size: 22px; font-weight: 700; }
  .signup-form__field:nth-of-type(3) { border-bottom: 1px solid var(--field-line); }

  .register-button {
    display: flex; align-items: center; justify-content: center;
    margin: 32px auto 0; width: 260px; height: 62px; border-radius: 31px;
    background: var(--brand-red-dark); font-size: 22px; font-weight: 400;
  }

  .cancel-bar {
    position: absolute; left: 0; right: 0; bottom: 0; height: 80px;
    background: var(--brand-red-dark);
    display: flex; align-items: center; justify-content: center;
    font-size: 22px; font-weight: 400;
  }
</style>
</head>
<body>
<main class="board">
  <header class="board-heading">
    <h1 class="board-heading__name">Vigilo</h1>
    <p class="board-heading__subtitle">Instan App Design</p>
    <p class="board-heading__tagline">modern, flat design</p>
  </header>

  <section class="signup-screen" aria-label="Sign up screen">
    <div class="status-bar">
      <span class="status-bar__carrier">
        <svg width="30" height="7" viewBox="0 0 30 7" aria-hidden="true">
          <circle cx="3" cy="3.5" r="2.6" fill="#fff"/>
          <circle cx="9" cy="3.5" r="2.6" fill="#fff"/>
          <circle cx="15" cy="3.5" r="2.6" fill="#fff"/>
          <circle cx="21" cy="3.5" r="2.2" fill="none" stroke="#fff" stroke-width="0.8"/>
          <circle cx="27" cy="3.5" r="2.2" fill="none" stroke="#fff" stroke-width="0.8"/>
        </svg>
        Vigilo
        <svg width="13" height="10" viewBox="0 0 13 10" aria-hidden="true">
          <path d="M1 3.5a8 8 0 0 1 11 0M3 5.8a5 5 0 0 1 7 0" fill="none" stroke="#fff" stroke-width="1.3" stroke-linecap="round"/>
          <circle cx="6.5" cy="8.3" r="1.2" fill="#fff"/>
        </svg>
      </span>
      <span class="status-bar__time">4:21 PM</span>
      <span class="status-bar__battery">
        100%
        <svg width="24" height="11" viewBox="0 0 24 11" aria-hidden="true">
          <rect x="0.5" y="0.5" width="20" height="10" rx="2" fill="none" stroke="#fff"/>
          <rect x="2" y="2" width="17" height="7" rx="1" fill="#fff"/>
          <rect x="21.5" y="3.5" width="2" height="4" rx="1" fill="#fff"/>
        </svg>
      </span>
    </div>

    <svg class="avatar" viewBox="0 0 128 128" role="img" aria-label="Profile picture placeholder">
      <defs><clipPath id="avatar-clip"><circle cx="64" cy="64" r="55"/></clipPath></defs>
      <circle cx="64" cy="64" r="59" fill="var(--brand-red-dark)" stroke="#fff" stroke-width="7"/>
      <g clip-path="url(#avatar-clip)" fill="#fff">
        <circle cx="64" cy="47" r="19"/>
        <rect x="22" y="72" width="84" height="70" rx="34"/>
      </g>
    </svg>

    <form class="signup-form">
      <div class="signup-form__field">full name</div>
      <div class="signup-form__field">email address</div>
      <div class="signup-form__field signup-form__field--password">••••••••</div>
      <div class="register-button">Register</div>
    </form>

    <div class="cancel-bar">Cancel</div>
  </section>

  <div class="screen-label">Sign Up Screen</div>
</main>
</body>
</html>
```